Web Developer Needs a Business Card Design

I need a personal business card design that represents me as a web developer for potential employers. I would like the background to be a dark color on the front for contrast with my logo and name. The back will have all my information along with a smaller version of the logo. I want something with a modern look and feel, not too conservative. This will be used for potential employers and freelance work.

Industry/Entity Type

Business

Contact Information for Business Card

Front should have my logo and name. The back should have all my personal information which would include: name: Tom Brevardi, phone: 570-614-9083, email: tombrevardi@mailwisp.com, website url: www.tombrevardi.com, logo, web developer.

Font styles to use
Sans Serif

Requirements
Must have
• Must include my logo. The color palette base color will be the logo color.

```html
<!DOCTYPE html>
<html lang="en">
<head>
<meta charset="utf-8">
<title>Tom Brevardi — Business Card</title>
<link href="https://fonts.googleapis.com/css2?family=Open+Sans:wght@400;600&display=swap" rel="stylesheet">
<style>
  :root {
    --backdrop: #e9e4dc;
    --card: #f7f7f6;
    --teal: #7fd0c4;
    --teal-deep: #5dbdae;
    --teal-soft: #a9e0d7;
    --ink: #1b1b1b;
    --muted: #555a5a;
  }
  html, body {
    margin: 0;
    width: 1200px;
    height: 902px;
    overflow: hidden;
    background: var(--backdrop);
    font-family: "Open Sans", sans-serif;
  }
  .canvas { position: relative; width: 1200px; height: 902px; }
  .card {
    position: absolute;
    width: 560px;
    height: 320px;
    background: var(--card);
    box-shadow: 0 3px 0 #dcdcdc, 0 6px 0 #cfcfcf, 0 14px 30px rgba(0,0,0,.18);
    overflow: hidden;
  }
  .card-front { left: 60px; top: 70px; }
  .card-back { left: 580px; top: 500px; }
  .card-bands { position: absolute; inset: 0; }
  .band-top { fill: var(--teal-soft); }
  .band-bottom { fill: var(--teal-deep); }

  .brand-mark {
    position: absolute;
    display: flex;
    align-items: center;
    gap: 10px;
    color: var(--teal-deep);
    font-weight: 400;
  }
  .brand-dot {
    border: 6px solid var(--teal);
    border-radius: 50%;
    box-sizing: border-box;
  }
  .card-front .brand-mark { left: 0; right: 0; top: 80px; justify-content: center; font-size: 20px; }
  .card-front .brand-dot { width: 70px; height: 70px; }
  .front-name {
    position: absolute; left: 0; right: 0; top: 178px;
    text-align: center; font-size: 32px; color: var(--ink); margin: 0; font-weight: 400;
  }

  .card-back .brand-mark { left: 40px; top: 120px; flex-direction: column; font-size: 16px; width: 190px; }
  .card-back .brand-dot { width: 86px; height: 86px; }
  .divider { position: absolute; left: 250px; top: 90px; width: 2px; height: 150px; background: var(--ink); }
  .identity { position: absolute; left: 275px; top: 88px; }
  .identity-name { margin: 0; font-size: 30px; font-weight: 400; color: var(--teal); line-height: 1.1; }
  .identity-role { margin: 0 0 0 4px; font-size: 13px; color: var(--muted); }
  .contact-list { position: absolute; left: 278px; top: 168px; margin: 0; padding: 0; list-style: none; }
  .contact-list li { display: flex; align-items: center; gap: 8px; font-size: 14px; color: var(--ink); height: 22px; }
  .contact-icon { width: 13px; height: 13px; background: var(--ink); border-radius: 2px; display: flex; align-items: center; justify-content: center; }
  .contact-icon svg { width: 9px; height: 9px; fill: #fff; }
</style>
</head>
<body>
<main class="canvas">

  <section class="card card-front" aria-label="Card front">
    <svg class="card-bands" viewBox="0 0 560 320" aria-hidden="true">
      <path class="band-top" d="M0 0H560V62Q280 -8 0 62Z"/>
      <path class="band-bottom" d="M0 240Q280 330 560 220V320H0Z"/>
    </svg>
    <div class="brand-mark"><span class="brand-dot"></span><span>Tom Brevardi</span></div>
    <h1 class="front-name">Tom Brevardi</h1>
  </section>

  <section class="card card-back" aria-label="Card back">
    <svg class="card-bands" viewBox="0 0 560 320" aria-hidden="true">
      <path class="band-top" d="M0 0H560V55Q280 -5 0 55Z"/>
      <path class="band-bottom" d="M0 250Q280 320 560 225V320H0Z"/>
    </svg>
    <div class="brand-mark"><span class="brand-dot"></span><span>Tom Brevardi</span></div>
    <div class="divider"></div>
    <div class="identity">
      <h2 class="identity-name">Tom Brevardi</h2>
      <p class="identity-role">web developer</p>
    </div>
    <ul class="contact-list">
      <li><span class="contact-icon"><svg viewBox="0 0 10 10"><path d="M2 1l2 2-1 1q1 2 3 3l1-1 2 2-1 1.5Q4 9 1 2.5Z"/></svg></span>570-614-9083</li>
      <li><span class="contact-icon"><svg viewBox="0 0 10 10"><circle cx="5" cy="5" r="4" fill="none" stroke="#fff" stroke-width="1.2"/><path d="M1 5h8M5 1v8" stroke="#fff" stroke-width="1"/></svg></span>www.tombrevardi.com</li>
      <li><span class="contact-icon"><svg viewBox="0 0 10 10"><path d="M1 2.5h8v5H1Z" fill="none" stroke="#fff" stroke-width="1"/><path d="M1 2.5l4 3 4-3" fill="none" stroke="#fff" stroke-width="1"/></svg></span>tombrevardi@mailwisp.com</li>
    </ul>
  </section>

</main>
</body>
</html>
```